Bref créative
VELMORA BUSINESS CARDS
VELMORA BC
Professional
Anselmo Tribaldes
Director General
Fidencio Lozano 4817. Local 5 Altos.
Colonia Almendros.
Nuevo Laredo, Tamaulipas 88172.
Mexico.
anselmo@velmora-ejemplo.com
www.velmora-ejemplo.com
* Importacion y Exportacion.
* Comercializacion y Procura.
* Transporte LTL, Van Trailers, Flatbed, Oversize cargo.
* Soluciones de logistica.
* Aduanas.
Vector Logo file

```html
<!DOCTYPE html>
<html lang="es">
<head>
<meta charset="utf-8">
<title>VELMORA Stationery</title>
<link href="https://fonts.googleapis.com/css2?family=Arimo:wght@400;700&display=swap" rel="stylesheet">
<style>
  :root{
    --bg-light:#9a9a9a; --bg-dark:#4a4a4a;
    --paper:#ffffff; --ink:#1b1f3a; --muted:#6b6f80;
    --brand-blue:#2b2fa8; --card-black:#111111; --label:#e6e6e6;
  }
  *{box-sizing:border-box;margin:0;padding:0}
  html,body{width:1200px;height:446px;overflow:hidden}
  body{font-family:"Arimo",Arial,sans-serif;color:var(--ink);
    background:radial-gradient(ellipse at 50% 40%,var(--bg-light),var(--bg-dark) 95%);position:relative}
  .wordmark{font-weight:700;color:var(--ink);letter-spacing:.5px;white-space:nowrap}
  .label{position:absolute;top:430px;font-size:8px;color:var(--label);text-align:center}

  .brand-intro{position:absolute;left:22px;top:142px;width:158px}
  .brand-intro .wordmark{font-size:24px}
  .brand-intro .tagline{font-size:12px;color:#eaeaea;margin-top:8px}

  .card{position:absolute;left:19px;width:158px;height:90px;box-shadow:0 2px 6px rgba(0,0,0,.5);overflow:hidden}
  .card-front{top:222px;background:var(--paper);padding:7px 9px;font-size:5px;line-height:1.4}
  .card-front .wordmark{font-size:13px;margin-bottom:5px}
  .card-front .name{font-weight:700;font-size:6px}
  .card-back{top:330px;background:var(--card-black);color:#ddd;padding:9px 9px;font-size:5.4px;line-height:1.75}

  .sheet{position:absolute;top:20px;width:300px;height:403px;background:var(--paper);box-shadow:0 2px 8px rgba(0,0,0,.45);overflow:hidden}
  .sheet .wordmark{position:absolute;top:18px;font-size:18px}
  .sheet .header-info{position:absolute;right:18px;top:18px;font-size:4px;line-height:1.5;color:var(--muted);text-align:right}
  .sheet .footer{position:absolute;left:0;right:0;bottom:12px;font-size:4px;color:var(--muted);text-align:center}

  .envelope{position:absolute;left:828px;width:300px;background:var(--paper);box-shadow:0 2px 6px rgba(0,0,0,.45);overflow:hidden}
  .envelope svg{position:absolute;left:0;top:0}
  .envelope .wordmark{position:absolute;left:12px;top:10px;font-size:15px}
  .envelope .return{position:absolute;right:12px;bottom:8px;font-size:4px;color:var(--muted)}
</style>
</head>
<body>

<section class="brand-intro">
  <div class="wordmark">VELMORA</div>
  <div class="tagline">Stationery Concepts</div>
</section>

<article class="card card-front">
  <div class="wordmark">VELMORA</div>
  <p class="name">Anselmo Tribaldes</p>
  <p>Director General</p>
  <p>Fidencio Lozano 4817. Local 5 Altos.</p>
  <p>Colonia Almendros.</p>
  <p>Nuevo Laredo, Tamaulipas 88172. Mexico.</p>
  <p>anselmo@velmora-ejemplo.com</p>
  <p>www.velmora-ejemplo.com</p>
</article>

<article class="card card-back">
  <p>* Importacion y Exportacion.</p>
  <p>* Comercializacion y Procura.</p>
  <p>* Transporte LTL, Van Trailers, Flatbed, Oversize cargo.</p>
  <p>* Soluciones de logistica.</p>
  <p>* Aduanas.</p>
</article>
<div class="label" style="left:19px;width:158px">Business Card</div>

<article class="sheet" style="left:192px">
  <div class="wordmark" style="left:26px">VELMORA</div>
  <div class="header-info">
    <p>Fidencio Lozano 4817. Local 5 Altos.</p>
    <p>Colonia Almendros. 88172</p>
    <p>Nuevo Laredo, Tamaulipas</p>
    <p>www.velmora-ejemplo.com</p>
  </div>
</article>
<div class="label" style="left:192px;width:300px">Letterhead 01</div>

<article class="sheet" style="left:504px">
  <div class="wordmark" style="left:50%;transform:translateX(-50%)">VELMORA</div>
  <div class="footer">Fidencio Lozano 4817. Local 5 Altos. Colonia Almendros. Nuevo Laredo, Tamaulipas 88172. www.velmora-ejemplo.com</div>
</article>
<div class="label" style="left:504px;width:300px">Letterhead 02</div>

<article class="envelope" style="top:20px;height:92px">
  <svg width="300" height="92" viewBox="0 0 300 92"><path d="M0 0H300V16L150 52L0 16Z" fill="var(--card-black)"/><circle cx="150" cy="28" r="8" fill="#fff"/></svg>
</article>
<article class="envelope" style="top:120px;height:92px">
  <svg width="300" height="92" viewBox="0 0 300 92"><path d="M0 0H300V16L150 52L0 16Z" fill="var(--brand-blue)"/><circle cx="150" cy="28" r="8" fill="#fff"/></svg>
</article>
<article class="envelope" style="top:220px;height:92px">
  <svg width="300" height="92" viewBox="0 0 300 92"><path d="M0 0H300V12L150 48L0 12Z" fill="#f4f4f4" stroke="#ddd"/><circle cx="150" cy="30" r="9" fill="var(--brand-blue)"/></svg>
</article>
<article class="envelope" style="top:320px;height:103px">
  <div class="wordmark">VELMORA</div>
  <div class="return">Fidencio Lozano 4817. Colonia Almendros. 88172</div>
</article>
<div class="label" style="left:828px;width:300px">Envelope Variations</div>

</body>
</html>
```